Book Cover design Paws & Petals Book Cover

Please see attached brief Book title BRAVE BESIDE TAILS AND TIDES
THE QUIET GIFT OF CANINES IN LIVING AND HEALING (INCLUSIVE OF THERAPY, EDUCATION, PARENTING, CARE) I have attached a word document describing the brief. Essentially book cover should include a dog and a person, perhaps an older person and a child, and a dog, emotionally charged faces, no cartoons, happy with designer to play with concept and ideas, please avoid AI looking images.

Target Market(s)

Parents, therapists, teachers, people who work with patients/vulnerable people

Industry/Entity Type

Therapeutic care, education, non fiction

Font styles to use
Sans Serif

Requirements
Must have
• Warmth, emotion. I have included the Author photo and paragraph for the back, and also the spec in the details.

```html
<!DOCTYPE html>
<html lang="en">
<head>
<meta charset="utf-8">
<title>Brave Beside Tails and Tides – Cover Spread</title>
<link rel="stylesheet" href="https://fonts.googleapis.com/css2?family=Playfair+Display:wght@400;500&family=Lora:ital@1&family=Questrial&display=swap">
<style>
  :root {
    --backdrop: #b3b3b3;
    --paper: #e3d6c2;
    --ink: #4a3131;
    --rust: #a9552e;
    --body-ink: #3a2a28;
    --art-light: #e9d3a8;
    --art-mid: #b98a55;
    --art-deep: #7b5433;
  }
  * { margin: 0; padding: 0; box-sizing: border-box; }
  html, body { width: 1200px; height: 882px; overflow: hidden; background: var(--backdrop); }
  .cover {
    position: absolute; left: 49px; top: 49px; width: 1102px; height: 783px;
    background: var(--paper);
    box-shadow: 0 2px 8px rgba(0,0,0,.18);
    color: var(--ink);
  }
  .title { position: absolute; text-align: center; font-family: "Playfair Display", serif; font-weight: 400; }
  .title .caps { display: block; }
  .title .small { display: block; }
  .title .accent { color: var(--rust); }

  .back-title { left: 108px; width: 300px; top: 52px; }
  .back-title .caps { font-size: 74px; line-height: 62px; }
  .back-title .small { font-size: 28px; line-height: 22px; }

  .front-title { left: 644px; width: 400px; top: 30px; }
  .front-title .caps { font-size: 101px; line-height: 86px; }
  .front-title .small { font-size: 38px; line-height: 31px; }

  .subtitle { position: absolute; text-align: center; font-family: "Lora", serif; font-style: italic; white-space: nowrap; }
  .subtitle .accent { color: var(--rust); }
  .back-subtitle { left: 58px; width: 400px; top: 293px; font-size: 15px; }
  .front-subtitle { left: 594px; width: 500px; top: 362px; font-size: 20px; }

  .blurb, .author-bio {
    position: absolute; font-family: "Questrial", sans-serif; font-size: 13px; line-height: 15.6px;
    color: var(--body-ink); text-align: justify; hyphens: auto;
  }
  .blurb { left: 31px; width: 452px; top: 351px; }
  .author-bio { left: 172px; width: 311px; top: 491px; }
  .blurb b, .author-bio b { font-style: italic; }
  .author-photo {
    position: absolute; left: 31px; top: 491px; width: 127px; height: 134px;
    background: radial-gradient(circle at 55% 40%, #c99a6c 0 22%, #3b3348 48%, #2a2430 100%);
  }

  .spine {
    position: absolute; left: 536px; top: 44px; writing-mode: vertical-rl;
    font-family: "Playfair Display", serif; white-space: nowrap;
  }
  .spine-title { font-size: 34px; line-height: 34px; }
  .spine-title .accent { color: var(--rust); }
  .spine-author { position: absolute; left: 538px; top: 621px; writing-mode: vertical-rl; font-family: "Playfair Display", serif; font-size: 13px; line-height: 15px; }

  .cover-art {
    position: absolute; left: 629px; top: 394px; width: 422px; height: 341px;
    border-radius: 48% 48% 44% 44% / 40% 40% 60% 60%;
    background: radial-gradient(ellipse at 60% 40%, var(--art-light) 0%, var(--art-mid) 55%, var(--art-deep) 85%, rgba(227,214,194,0) 100%);
  }
  .front-author {
    position: absolute; left: 594px; width: 500px; top: 737px; text-align: center;
    font-family: "Playfair Display", serif; font-size: 23px; color: #1f1816; letter-spacing: .2px;
  }
</style>
</head>
<body>
<main class="cover">
  <section class="back">
    <h2 class="title back-title">
      <span class="caps">BRAVE</span><span class="small">beside</span>
      <span class="caps accent">TAILS</span><span class="small">and</span>
      <span class="caps">TIDES</span>
    </h2>
    <p class="subtitle back-subtitle">The Quiet <span class="accent">Gift of Canines in Living</span> and Healing</p>
    <p class="blurb"><b>Brave Beside Tails and Tides</b> is a practical and reflective book about the role of dogs in everyday emotional life. It draws on real experience from therapeutic work, education, parenting, and care, showing how dogs offer consistency, comfort and connection during difficult times, and how they in general provide consistent support in growth and learning. It’s written for professionals, parents and carers who live or work alongside dogs in emotionally complex situations and want something honest, useful and grounded in real practice.</p>
    <div class="author-photo" role="img" aria-label="Portrait photo of the author"></div>
    <p class="author-bio"><b>Dr Helena Marsh</b> is the CEO of Larkfield. She leads national work in therapeutic education, trauma-informed care, and animal-assisted interventions. Helena has over 20 years’ experience across social work, mental health and leadership, and is a parent of three. Her work combines lived experience with professional insight, with a focus on what helps in real life not just in theory.</p>
  </section>

  <div class="spine spine-title">BRAVE beside <span class="accent">TAILS</span> and TIDES</div>
  <div class="spine-author">DR HELENA<br>MARSH</div>

  <section class="front">
    <h1 class="title front-title">
      <span class="caps">BRAVE</span><span class="small">beside</span>
      <span class="caps accent">TAILS</span><span class="small">and</span>
      <span class="caps">TIDES</span>
    </h1>
    <p class="subtitle front-subtitle">The Quiet <span class="accent">Gift of Canines in Living</span> and Healing</p>
    <div class="cover-art" role="img" aria-label="Painted illustration of a golden retriever and a young child facing each other in warm light"></div>
    <p class="front-author">DR HELENA MARSH</p>
  </section>
</main>
</body>
</html>
```